Larkin Ridge Provisions Co Website Creation

We need a website designed that goes along with our western/cattle brand vibe that our logo has. We are going to need a couple different pages including: About Us, Meat Boxes, Recipes, Contact Us.

We are going to need a shop so that people may visit the website and order meat boxes to be shipped or delivered at their home. Our mission is to provide the highest quality meat that every family can afford.

Would love to see the website design with lots of mountain range backgrounds and create a feel of open range beef that has a tradition of providing great beef. Family owned business that has been raising cattle for over 30 years.

Love the colors of using dark greens, browns, Tans, Blacks

```html
<!DOCTYPE html>
<html lang="en">
<head>
<meta charset="UTF-8">
<title>Larkin Ridge Provisions Co</title>
<link href="https://fonts.googleapis.com/css2?family=Lato:wght@400;700&family=Lora:wght@500;600&display=swap" rel="stylesheet">
<style>
  :root {
    --cream: #fbf5ee;
    --brown: #6a3a24;
    --brown-dark: #4e2816;
    --green-dark: #3b4a39;
    --green-mid: #566b43;
    --ink: #1f1c19;
    --muted: #5a534c;
    --white: #ffffff;
    --field: #f4f1ec;
  }
  * { box-sizing: border-box; margin: 0; padding: 0; }
  html, body { width: 1200px; height: 4100px; overflow: hidden; }
  body { position: relative; background: var(--cream); font-family: "Lato", sans-serif; color: var(--ink); }
  .abs { position: absolute; }
  .serif { font-family: "Lora", serif; }
  .btn { position: absolute; display: flex; align-items: center; justify-content: center; font-size: 13px; height: 40px; padding: 0 22px; border-radius: 2px; }
  .btn-brown { background: var(--brown); color: var(--white); }
  .btn-light { background: var(--white); color: var(--ink); }
  .photo { position: absolute; }

  /* Hero */
  .hero { left: 0; top: 0; width: 1200px; height: 660px;
    background: linear-gradient(180deg, #9bb0c2 0%, #c9d2cf 22%, #7f8f63 45%, #5d7a3a 70%, #3f5a28 100%); }
  .hero-shade { left: 0; top: 0; width: 1200px; height: 660px; background: linear-gradient(180deg, rgba(0,0,0,.25), rgba(0,0,0,.05) 60%, rgba(0,0,0,.1)); }
  .nav { left: 0; top: 0; width: 1200px; height: 70px; display: flex; align-items: center; justify-content: center; gap: 46px; color: var(--white); font-size: 14px; }
  .nav-rule { left: 260px; top: 70px; width: 680px; height: 1px; background: rgba(255,255,255,.5); }
  .brand { font-family: "Lato", sans-serif; font-weight: 700; font-size: 15px; text-align: center; line-height: 1.15; width: 130px; text-transform: uppercase; }
  .hero-title { left: 0; top: 170px; width: 1200px; text-align: center; color: var(--white); font-size: 46px; line-height: 1.2; font-weight: 600; }
  .hero-rule { left: 450px; top: 286px; width: 300px; height: 2px; background: rgba(255,255,255,.8); }
  .hero-sub { left: 0; top: 306px; width: 1200px; text-align: center; color: var(--white); font-size: 14px; }

  /* About */
  .about-title { left: 80px; top: 830px; width: 320px; font-size: 28px; line-height: 1.3; }
  .about-text { left: 80px; top: 950px; width: 300px; font-size: 13px; line-height: 1.65; color: var(--muted); }
  .about-photo { left: 440px; top: 800px; width: 330px; height: 500px; background: linear-gradient(180deg, #c5d3dc 0%, #8ea07a 30%, #5f7e3b 65%, #4a6a2c 100%); }
  .quote-rule { left: 880px; top: 920px; width: 2px; height: 240px; background: var(--ink); }
  .quote { left: 910px; top: 930px; width: 250px; font-size: 19px; line-height: 1.45; }
  .quote-author { left: 910px; top: 1120px; display: flex; align-items: center; gap: 10px; font-size: 12px; color: var(--muted); }
  .quote-author span.line { width: 40px; height: 1px; background: var(--muted); }

  /* Meat boxes */
  .section-title { left: 0; width: 1200px; text-align: center; font-size: 40px; line-height: 1.25; font-weight: 600; }
  .section-text { left: 340px; width: 520px; text-align: center; font-size: 13px; line-height: 1.6; color: var(--muted); }
  .box-card { position: absolute; top: 1580px; width: 332px; height: 460px; background: var(--white); }
  .box-photo { left: 0; top: 0; width: 332px; height: 340px; background: linear-gradient(150deg, #3a2a20 0%, #7a2a24 45%, #a9443a 65%, #4a3226 100%); }
  .box-name { left: 20px; top: 340px; height: 120px; width: 180px; display: flex; align-items: center; font-size: 18px; line-height: 1.3; }
  .box-card .btn { right: 20px; top: 382px; height: 36px; padding: 0 16px; font-size: 12px; }

  /* Recipes */
  .recipe-feature { left: 80px; top: 2388px; width: 424px; height: 572px; background: linear-gradient(180deg, #181a17 0%, #2a2520 40%, #8a5a2e 55%, #4a5a30 68%, #2f3a2b 100%); }
  .recipe-overlay { left: 80px; top: 2760px; width: 424px; height: 200px; background: rgba(52,68,48,.82); }
  .recipe-name { left: 110px; top: 2784px; color: var(--white); font-size: 18px; font-weight: 700; }
  .recipe-desc { left: 110px; top: 2816px; width: 240px; color: rgba(255,255,255,.85); font-size: 12px; line-height: 1.55; }
  .recipe-link { left: 110px: top: 0; }
  .recipe-top { left: 520px; top: 2388px; width: 596px; height: 272px; background: linear-gradient(135deg, #5d7a2f 0%, #8a5530 40%, #a86a3e 60%, #c9c1b0 100%); }
  .recipe-bottom { left: 520px; top: 2680px; width: 596px; height: 280px; background: linear-gradient(135deg, #1e1c1a 0%, #3a2c24 40%, #6a3a26 60%, #2a2622 100%); }

  /* CTA */
  .cta { left: 0; top: 3180px; width: 1200px; height: 340px; background: linear-gradient(180deg, #a9b8bf 0%, #7f9462 35%, #5f7f35 65%, #44662a 100%); }
  .cta-shade { left: 0; top: 3180px; width: 1200px; height: 340px; background: linear-gradient(90deg, rgba(0,0,0,.35), rgba(0,0,0,.1) 70%); }
  .cta-title { left: 168px; top: 3280px; width: 480px; color: var(--white); font-size: 32px; line-height: 1.2; font-weight: 600; }
  .cta-text { left: 168px; top: 3370px; width: 380px; color: rgba(255,255,255,.9); font-size: 13px; line-height: 1.5; }

  /* Contact */
  .contact { left: 0; top: 3520px; width: 1200px; height: 580px; background: var(--green-dark); }
  .contact-title { color: var(--white); font-size: 36px; font-weight: 500; }
  .field { position: absolute; background: var(--white); border-radius: 2px; font-size: 12px; color: #8a857d; padding: 12px 12px; }
  .divider { left: 600px; top: 3600px; width: 1px; height: 440px; background: rgba(255,255,255,.5); }
  .info-label { color: var(--white); font-size: 18px; }
  .info-value { color: rgba(255,255,255,.85); font-size: 13px; }
  .footer-links { display: flex; gap: 22px; color: rgba(255,255,255,.85); font-size: 13px; }
</style>
</head>
<body>

<!-- Hero -->
<div class="abs photo hero" role="img" aria-label="Cattle grazing on green pastures beneath a mountain range"></div>
<div class="abs hero-shade"></div>
<nav class="abs nav">
  <span>About Us</span>
  <span>Meat Boxes</span>
  <span class="brand">Larkin Ridge Provisions Co</span>
  <span>Recipes</span>
  <span>Contact Us</span>
</nav>
<div class="abs nav-rule"></div>
<h1 class="abs hero-title serif">Tradition of Excellence in Beef<br>Over 30 Years</h1>
<div class="abs hero-rule"></div>
<p class="abs hero-sub">Family-raised, grass-fed beef from our ranch to your table</p>
<div class="btn btn-brown" style="left:432px;top:392px;">Shop Meat Boxes</div>
<div class="btn btn-light" style="left:608px;top:392px;">Discover Our Story</div>

<!-- About -->
<h2 class="abs about-title serif">Raising Cattle with Care for Over 30 Years</h2>
<p class="abs about-text">Our story began over 30 years ago with a simple goal: to provide the highest quality beef that every family can enjoy. As a family-owned and operated business, we take pride in every step of the process, from raising our cattle in a sustainable environment to delivering our premium cuts directly to your home.</p>
<div class="btn btn-brown" style="left:80px;top:1228px;">Explore Our Ranch</div>
<div class="abs photo about-photo" role="img" aria-label="Herd of cattle grazing on a hillside valley"></div>
<div class="abs quote-rule"></div>
<p class="abs quote serif">Our family has always believed that quality beef starts with the way we treat our land and animals. It's a tradition we're proud to continue</p>
<div class="abs quote-author"><span class="line"></span><span>Wade Harlan</span></div>

<!-- Meat boxes -->
<h2 class="abs section-title serif" style="top:1425px;">Choose Your Meat Box</h2>
<p class="abs section-text" style="top:1492px;">Choose from a variety of carefully curated meat boxes, designed to suit every need. From premium steaks to ground beef, each box is packed with care and shipped fresh to ensure top-notch quality in every bite.</p>

<div class="box-card" style="left:80px;">
  <div class="abs photo box-photo" role="img" aria-label="Raw steaks arranged on a wooden board"></div>
  <div class="abs box-name serif">Family Feast Box</div>
  <div class="btn btn-brown">Add to Cart</div>
</div>
<div class="box-card" style="left:434px;">
  <div class="abs photo box-photo" role="img" aria-label="Raw steak with a knife and fork"></div>
  <div class="abs box-name serif">Grill Master's Choice</div>
  <div class="btn btn-brown">Add to Cart</div>
</div>
<div class="box-card" style="left:788px;">
  <div class="abs photo box-photo" role="img" aria-label="Cuts of raw beef with a cleaver"></div>
  <div class="abs box-name serif">Steak Lover's Selection</div>
  <div class="btn btn-brown">Add to Cart</div>
</div>
<div class="btn btn-brown" style="left:514px;top:2080px;">Browse All Meat Boxes</div>

<!-- Recipes -->
<h2 class="abs section-title serif" style="top:2244px;">Delicious Recipes to Elevate<br>Your Meat Experience</h2>
<div class="abs photo recipe-feature" role="img" aria-label="Beef burger with lettuce and tomato"></div>
<div class="abs recipe-overlay"></div>
<div class="abs recipe-name">Classic Beef Burger</div>
<p class="abs recipe-desc">A juicy beef patty grilled to perfection and served on a soft bun with fresh toppings.</p>
<div class="abs" style="left:110px;top:2872px;color:#fff;font-size:12px;display:flex;align-items:center;gap:6px;">Explore More
  <svg width="14" height="10" viewBox="0 0 14 10"><path d="M0 5h12M8 1l4 4-4 4" stroke="#fff" fill="none" stroke-width="1.3"/></svg>
</div>
<div class="abs photo recipe-top" role="img" aria-label="Sliced grilled steak with fresh salad"></div>
<div class="abs photo recipe-bottom" role="img" aria-label="Seared steak with fries in a cast-iron pan"></div>
<div class="btn btn-brown" style="left:500px;top:3008px;">Explore All Recipes</div>

<!-- CTA -->
<div class="abs photo cta" role="img" aria-label="Cattle on open range with trees and hills"></div>
<div class="abs cta-shade"></div>
<h2 class="abs cta-title serif">Join Our Family of Satisfied Customers</h2>
<p class="abs cta-text">Be part of our tradition and taste the difference of ranch-raised beef at your table.</p>
<div class="btn btn-brown" style="left:832px;top:3328px;width:200px;">Order Your Meat Box</div>

<!-- Contact -->
<div class="abs contact"></div>
<h2 class="abs contact-title serif" style="left:80px;top:3600px;width:420px;text-align:center;">Get in Touch</h2>
<div class="field" style="left:80px;top:3692px;width:202px;height:40px;">Name</div>
<div class="field" style="left:298px;top:3692px;width:202px;height:40px;">Email</div>
<div class="field" style="left:80px;top:3752px;width:420px;height:40px;">Phone Number</div>
<div class="field" style="left:80px;top:3812px;width:420px;height:160px;">Note</div>
<div class="btn btn-light" style="left:340px;top:3988px;width:160px;height:42px;">Send Message</div>

<div class="abs divider"></div>

<h2 class="abs contact-title serif" style="left:696px;top:3600px;">Contact Us</h2>
<div class="abs info-label" style="left:696px;top:3690px;">Address</div>
<div class="abs info-value" style="left:696px;top:3718px;">48 Sagebrush Lane, Cedar Bluff, MT</div>
<div class="abs info-label" style="left:696px;top:3752px;">Phone</div>
<div class="abs info-value" style="left:696px;top:3780px;">(406) 555-0148</div>
<div class="abs info-label" style="left:696px;top:3814px;">Email</div>
<div class="abs info-value" style="left:696px;top:3842px;">hello@larkinridge.com</div>
<div class="abs footer-links" style="left:696px;top:3890px;"><span>About Us</span><span>Meat Boxes</span><span>Recipes</span><span>Contact Us</span></div>
<div class="abs footer-links" style="left:696px;top:3918px;"><span>Privacy Policy</span><span>Term Of Service</span></div>

</body>
</html>
```